Kovri DIGITAL HORIZON learning portal

We beed a flyer design to launch our new DIGITAL HORIZON Learning Portal. The flyer will be used in letter box drops and to give to small business to encourage sales of this new service.

ABOUT US:

We are a small training firm offering world class training solutions in the areas of:

1. Time Management
2. Sales skills
3. Strategic & High performance leadership
4. Sales Management
5. Personal Maximum Achievement.

You can find our website at www.kovri.com.au

ABOUT DIGITAL HORIZON Learning Portal:

We are launching an online learning portal called DIGITAL HORIZON Learning Portal which will allow anyone, anywhere in the world to take our courses online as long as they have access to a PC, smart phone and internet.

Taking an online course with Kovri through our DIGITAL HORIZON Learning Portal will allow students/participants to save over 50% of the normal price of attending a face to face training program.

There are over 80 different individual learning units that can be taken by a student/participant. The participant can choose to take any unit they wish building their own unique learning experience or they can take a full course in one of the subject areas listed above in the about us section.

ADVANTAGES OF USING THE Kovri DIGITAL HORIZON Learning Portal:

* Cost effective, save over 50% by learning online compared to attending a Kovri class room based programme.
* learning can be scheduled around work and family
* Reduces travel time and travel costs
* Students/participants have the option to select learning materials that meets their level of knowledge and interest.
* Complete flexibility to build a personalised learning experience.
* Students/participants can study anywhere they have access to a computer and Internet connection
* Self-paced learning modules allow students/participants to work at their own pace
* Develops knowledge of the Internet and computers skills that will help learners throughout their lives and careers
* Successfully completing online or computer-based courses builds self-knowledge and self-confidence and encourages students to take responsibility for their learning
* Join over 4 million people who have successfully undertaken the training world wide at a time & a place convenient to students/participants.
* pay securely using zentrapay
* learn based on a students/participants personal financial circumstances with individual units priced at $82.50 each (this is Australian dollars & includes GST)

The final design will be one that conveys flexibility of learning, cost effectiveness of the online learning solution. The flyer design can either be folded, single or double sided, A4 or A5 or DL size - whatever works best in the final outcome.

Industry/Entity Type

Small Business

Requirements
Must have
• The flyer must include:

* the "DIGITAL HORIZON Learning portal" logo and the "Kovri logo" and use the Kovri font. Several logos have been provided and the most appropriate ones can be chosen for the design. The font has been provided. (I do have other logo files in different file formats if required to aid designers)

* The flyer must direct people to the Kovri website www.kovri.com.au to pay, enrol and find out other information about the courses.

* The flyer must highlight cost effectiveness of the solution, the world wide popularity of the programs (over 4 million people have completed the programs world wide), flexibility of learning & the diversity of study areas.

Because of price changes in future of courses it would be very beneficial to be able to edit files in future to show new prices if and when that happens.

```html
<!DOCTYPE html>
<html lang="en">
<head>
<meta charset="utf-8">
<title>Kovri – DIGITAL HORIZON Learning Portal flyer</title>
<link href="https://fonts.googleapis.com/css2?family=Open+Sans:wght@400;600;700&family=Great+Vibes&display=swap" rel="stylesheet">
<style>
  :root{
    --bg:#4a3128;
    --teal:#1f9a94;
    --teal-deep:#167f7a;
    --teal-pale:#c4e6e3;
    --ink:#2b2b2b;
    --black:#1a1a1a;
    --white:#ffffff;
    --grey:#8a8a8a;
  }
  *{box-sizing:border-box;margin:0;padding:0}
  html,body{width:1200px;height:889px;overflow:hidden}
  body{background:var(--bg);font-family:"Open Sans",Arial,sans-serif;color:var(--ink);position:relative}

  .page{position:absolute;top:130px;width:420px;height:600px;background:var(--white);overflow:hidden;box-shadow:0 6px 20px rgba(0,0,0,.35)}
  .page--front{left:160px}
  .page--back{left:620px}

  /* front */
  .hero{position:absolute;left:0;top:0;width:100%;height:320px;background:var(--teal-pale)}
  .hero__block{position:absolute;right:0;top:0;width:190px;height:150px;background:var(--teal)}
  .portal-badge{position:absolute;right:22px;top:24px;width:150px;height:40px;background:var(--black);display:flex;align-items:center;justify-content:center;gap:6px;color:var(--white);font-weight:700;font-size:12px;letter-spacing:.5px}
  .portal-badge__mark{width:8px;height:8px;background:var(--teal-pale)}
  .hero__collage{position:absolute;left:0;top:0}
  .subjects{position:absolute;left:0;top:320px;width:100%;list-style:none}
  .subjects li{height:32px;margin-bottom:6px;background:var(--teal);color:var(--white);font-family:"Great Vibes",cursive;font-size:24px;line-height:32px;padding-left:14px;white-space:nowrap}
  .subjects li:nth-child(1){margin-left:150px}
  .subjects li:nth-child(2){margin-left:125px}
  .subjects li:nth-child(3){margin-left:100px}
  .subjects li:nth-child(4){margin-left:75px}
  .subjects li:nth-child(5){margin-left:50px}

  /* back */
  .topbar{position:absolute;left:20px;right:0;top:14px;height:12px;background:var(--black);border-radius:6px 0 0 6px}
  .topbar__stripe{position:absolute;left:40px;right:0;top:26px;height:5px;background:var(--teal)}
  .col{position:absolute;top:42px;font-size:5.6px;line-height:1.45}
  .col--about{left:18px;width:205px}
  .col--clients{left:238px;width:168px}
  .col h2{font-size:6px;font-weight:600;margin-bottom:4px}
  .col p{margin-bottom:5px}
  .advantages{list-style:none}
  .advantages li{padding-left:6px;position:relative;margin-bottom:1px}
  .advantages li::before{content:"";position:absolute;left:0;top:3px;width:2.5px;height:2.5px;border-radius:50%;background:var(--ink)}
  .client-marks{display:grid;grid-template-columns:repeat(4,auto);gap:6px 8px;margin:12px 0 18px;font-size:8px;font-weight:700;color:var(--ink)}
  .brand{display:flex;align-items:center;gap:10px;margin-left:4px}
  .brand__mark{width:40px;height:40px;background:var(--teal)}
  .brand__name{font-size:30px;font-weight:400;color:var(--ink)}
  .contact{margin-top:8px;font-size:6.4px;line-height:1.5}
  .contact a{color:#2a4bb0}
  .crowd{position:absolute;left:0;bottom:0;width:100%;height:200px;background:linear-gradient(180deg,#b9b9b9 0%,#6f6f6f 40%,#2a2a2a 100%)}
</style>
</head>
<body>

<section class="page page--front">
  <div class="hero">
    <svg class="hero__collage" width="420" height="320" viewBox="0 0 420 320">
      <circle cx="160" cy="170" r="150" fill="#9fb6b4" role="img" aria-label="Circular collage of learners and graduates photographs"/>
      <defs><path id="arc" d="M60 250 A125 125 0 0 0 285 170"/></defs>
      <text font-family="Open Sans, Arial, sans-serif" font-size="9" fill="#2b2b2b">
        <textPath href="#arc">over 4 million people have completed the programs world wide</textPath>
      </text>
      <line x1="160" y1="170" x2="215" y2="158" stroke="#2a7bd1" stroke-width="3"/>
    </svg>
    <div class="hero__block">
      <div class="portal-badge"><span class="portal-badge__mark"></span>DIGITAL HORIZON</div>
    </div>
  </div>
  <ul class="subjects">
    <li>Time Management</li>
    <li>Sales skills</li>
    <li>Strategic &amp; High performance leadership</li>
    <li>Sales Management</li>
    <li>Personal Maximum Achievement</li>
  </ul>
</section>

<section class="page page--back">
  <div class="topbar"></div>
  <div class="topbar__stripe"></div>

  <div class="col col--about">
    <h2>ABOUT DIGITAL HORIZON Learning Portal:</h2>
    <p>We are launching an online learning portal called DIGITAL HORIZON Learning Portal which will allow anyone, anywhere in the world to take our courses online as long as they have access to a PC, smart phone and internet.</p>
    <p>Taking an online course with Kovri through our DIGITAL HORIZON Learning Portal will allow students/participants to save over 50% of the normal price of attending a face to face training program.</p>
    <p>There are over 80 different individual learning units that can be taken by a student/participant. The participant can choose to take any unit they wish building their own unique learning experience or they can take a full course in one of the subject areas.</p>
    <h2>ADVANTAGES OF USING THE Kovri DIGITAL HORIZON Learning Portal:</h2>
    <ul class="advantages">
      <li>Cost effective, save over 50% by learning online compared to attending a Kovri class room based programme.</li>
      <li>Learning can be scheduled around work and family</li>
      <li>Reduces travel time and travel costs</li>
      <li>Students/participants have the option to select learning materials that meets their level of knowledge and interest.</li>
      <li>Complete flexibility to build a personalised learning experience.</li>
      <li>Students/participants can study anywhere they have access to a computer and Internet connection</li>
      <li>Self-paced learning modules allow students/participants to work at their own pace</li>
      <li>Develops knowledge of the Internet and computers skills that will help learners throughout their lives and careers</li>
      <li>Successfully completing online or computer-based courses builds self-knowledge and self-confidence and encourages students to take responsibility for their learning</li>
      <li>Join over 4 million people who have successfully undertaken the training world wide at a time &amp; a place convenient to students/participants.</li>
      <li>Pay securely using zentrapay</li>
      <li>Learn based on a students/participants personal financial circumstances with individual units priced at $82.50 each (this is Australian dollars &amp; includes GST)</li>
    </ul>
  </div>

  <div class="col col--clients">
    <h2>Our Clients include:</h2>
    <p>Arvena Communications Network, Tallis, Corvane, Mirabel Group, Brightfield, Solace Homes, Quenton Bank, Harlow Motors, Venta Foods, Ostrell, Kaldor Systems, Pinemark, Larkspur Insurance, Northway Post, Elsby Freight, Torrin Energy, Castell Finance, Redgum Retail, Avalo Telecom, Brennick &amp; Co, Fenwick Logistics and Halden Partners.</p>
    <div class="client-marks">
      <span>Harlow</span><span>Quenton</span><span>Corvane</span><span>Kaldor</span>
      <span>Brennick</span><span>Solace</span><span>Torrin</span>
    </div>
    <div class="brand"><span class="brand__mark"></span><span class="brand__name">Kovri</span></div>
    <div class="contact">
      14/27 Harrow Lane Marlby, NSW 2099<br>
      Phone : +61 2 5550 174<br>
      <a href="mailto:sam.trellis@kovri.com.au">sam.trellis@kovri.com.au</a><br>
      nora.vance@kovri.com.au<br>
      www.kovri.com.au
    </div>
  </div>

  <div class="crowd" role="img" aria-label="Silhouette of a cheering crowd with raised hands"></div>
</section>

</body>
</html>
```